The Fern Barrel Pub- restaurant menu, new launch

This is a new restaurant launching Summer 2017. Restaurant is a conversion of long standing small town existing family pizza/italian restaurant. new concept shifts concept to a family pub atmosphere featuring familiar appetizers, burgers, wood-fired pizza, and daily specials, draft beer, full- bar.

atmosphere is casual. want menu to reflect a more current "vibe" than the old place did. Not cold and modern, but retain the cozy familiar feel, without seeming dated and old fashioned.

4 panel menu; 8.5 X 11; 2-4 color
Updates

Project Deadline Extended
Reason: I am interested in seeing more designs. I will be providing feedback in the next few days on all designs submitted. I will also be increasing the budget.

Target Market(s)

Family-Oriented Pub, rural location Berkshire County, MA. Mostly Blue collar customer, value oriented

Industry/Entity Type

American Restaurant

Font styles to use
Sans Serif

Colors

Designer to choose colors to be used in the design.

Requirements
Must have
• Clear, uncluttered design, Highlighted items as specified in draft file (to come)
• ability to make changes daily as menu changes
• each panel separate sheet to slide into binder sleeve

```html
<!DOCTYPE html>
<html lang="en">
<head>
<meta charset="utf-8">
<title>Wood Fired Pizza – The Fern Barrel Pub</title>
<link rel="stylesheet" href="https://fonts.googleapis.com/css2?family=Bowlby+One&family=Rye&family=Bebas+Neue&family=Abril+Fatface&family=Cabin:wght@500;600&display=swap">
<style>
  :root {
    --paper: #d9bf8c;
    --paper-dark: #c3a270;
    --paper-light: #fbf3e2;
    --brown: #4d3322;
    --ink: #1c1510;
    --white: #ffffff;
  }
  * { margin: 0; padding: 0; box-sizing: border-box; }
  html, body { width: 927px; height: 1200px; overflow: hidden; }
  body {
    position: relative;
    background: radial-gradient(ellipse at 45% 55%, var(--paper-light) 0%, #efdfbd 35%, var(--paper) 70%, var(--paper-dark) 100%);
    color: var(--ink);
    font-family: "Cabin", sans-serif;
  }
  .paper-glow {
    position: absolute; left: 52px; top: 72px; width: 824px; height: 676px;
    background: radial-gradient(ellipse at 40% 60%, rgba(255,255,255,0.85) 0%, rgba(255,255,255,0.45) 55%, rgba(255,255,255,0.2) 100%);
  }
  .abs { position: absolute; }
  .title-main {
    left: 54px; top: 66px; white-space: nowrap; color: var(--brown);
    font-family: "Bowlby One", sans-serif; font-size: 112px; line-height: 1; font-weight: 400;
    transform: scaleX(0.62); transform-origin: left top;
  }
  .title-script {
    left: 588px; top: 62px; white-space: nowrap; color: var(--brown);
    font-family: "Rye", serif; font-size: 88px; line-height: 1.1; font-weight: 400;
  }
  .intro { left: 54px; top: 198px; width: 815px; font-size: 16px; font-weight: 600; line-height: 22px; }
  .rule { left: 56px; width: 820px; height: 2px; background: var(--brown); }
  .section-head {
    left: 56px; font-family: "Bebas Neue", sans-serif; font-size: 66px; line-height: 1;
    white-space: nowrap; letter-spacing: 3.6px; font-weight: 400;
  }
  .pie-name { left: 54px; white-space: nowrap; line-height: 1; font-size: 46px; transform-origin: left top; }
  .squeeze { transform: scaleX(0.82); }
  .heavy { font-family: "Bowlby One", sans-serif; }
  .fat { font-family: "Abril Fatface", serif; }
  .narrow { font-family: "Bebas Neue", sans-serif; font-size: 58px; }
  .pie-desc { left: 453px; width: 420px; font-size: 16px; font-weight: 500; line-height: 21.6px; }
  .col-head { font-family: "Abril Fatface", serif; font-size: 23px; line-height: 25px; font-weight: 400; }
  .col-list { font-size: 16px; font-weight: 500; line-height: 21.6px; text-transform: uppercase; }
  .fold-band {
    left: 56px; top: 1068px; width: 816px; height: 80px; border-radius: 14px;
    background: var(--brown); color: var(--white);
    display: flex; align-items: center;
  }
  .fold-title { font-family: "Bebas Neue", sans-serif; font-size: 66px; letter-spacing: 13px; width: 398px; padding-left: 6px; white-space: nowrap; }
  .fold-text { font-size: 16px; font-weight: 500; line-height: 22px; width: 380px; }
</style>
</head>
<body>
  <div class="paper-glow"></div>

  <h1>
    <span class="abs title-main">WOOD FIRED</span>
    <span class="abs title-script">Pizza</span>
  </h1>
  <p class="abs intro">All our dough is made fresh daily in house with just four ingredients- water flour salt and yeast.&nbsp; Baked to perfection in the wood over, Fern Barrel Pizza is the best in the county!</p>
  <div class="abs rule" style="top:262px"></div>

  <h2 class="abs section-head" style="top:292px">Our Specialty Pies- SM$13&nbsp; LG$17</h2>

  <div class="abs pie-name squeeze" style="top:378px"><span class="heavy" style="font-size:42px">THE BUFFALO</span> <span class="fat" style="font-size:48px">Bird</span></div>
  <p class="abs pie-desc" style="top:380px">Buffalo sauce, grilled chicken, mozzarella and topped with red onion for just the right finish.&nbsp; Don't like onion?&nbsp; We'll leave it off!</p>

  <div class="abs pie-name squeeze" style="top:450px"><span class="heavy" style="font-size:44px">CHICKEN</span> <span class="fat" style="font-size:52px">'Q</span></div>
  <p class="abs pie-desc" style="top:462px">House made BBQ sauce from Red Hollow BBQ, Grilled chicken and mozzarella make this crowd favorite.</p>

  <div class="abs pie-name" style="top:520px;font-size:54px"><span class="fat">The</span><span class="narrow" style="font-size:64px">HULA</span><span class="fat">Hula</span></div>
  <p class="abs pie-desc" style="top:526px">Sliced ham and Pineapple, and mozzarella.&nbsp; It doesn't get any better!<br>ASK FOR COCONUT, IF YOU'RE FEELING CRAZY!</p>

  <div class="abs pie-name" style="top:594px;font-size:54px"><span class="narrow" style="font-size:64px">WHITE</span> <span class="fat">Pizza</span></div>
  <p class="abs pie-desc" style="top:608px">House made BBQ sauce from Red Hollow BBQ, Grilled chicken and mozzarella make this crowd favorite.</p>

  <div class="abs pie-name heavy squeeze" style="top:674px;font-size:40px">SICILIAN BOSS</div>
  <p class="abs pie-desc" style="top:677px">House made BBQ sauce from Red Hollow BBQ, Grilled chicken and mozzarella make this crowd favorite.</p>

  <div class="abs rule" style="top:746px"></div>

  <h2 class="abs section-head" style="top:758px">Create Your Own- SM$11&nbsp; LG$15</h2>

  <h3 class="abs col-head" style="left:57px;top:845px">Choose from standard<br>toppings for $2.00:</h3>
  <p class="abs col-list" style="left:57px;top:920px;width:262px">Pepperoni, onion, tomato, garlic, green pepper, mushroom, sliced or chopped tomato, broccoli, spinach, sliced black olives</p>

  <h3 class="abs col-head" style="left:334px;top:845px">More Meats $2.50:</h3>
  <p class="abs col-list" style="left:335px;top:892px;width:255px">Meatball, bacon, sausage, chicken, ham</p>
  <p class="abs col-list" style="left:337px;top:1002px;width:255px">Gluten free, available in small size only- add $2.00</p>

  <h3 class="abs col-head" style="left:612px;top:845px">Specialty Toppings<br>$3.00:</h3>
  <p class="abs col-list" style="left:613px;top:918px;width:232px">Xtra cheese, pineapple, feta, ricotta, kalamata olives, hot peppers, coconut, artichokes, sun dried tomato, pesto</p>

  <div class="abs fold-band">
    <div class="fold-title">Fold it Up!</div>
    <p class="fold-text">Turn your Pizza into a calzone, specialty or build your own.&nbsp; Same price as a small.</p>
  </div>
</body>
</html>
```